DOG DAYCARE BILLBOARD

Design a bold exciting billboard that can be read easily from a distance! Our goal is brand awareness and showcasing the services we offer (Boarding, Grooming, Daycare, and Training.
we would like to see examples with the phrase "your best friend's best day". Our name Bright Meadow Canine Activity Center (or just Bright Meadow might work better and could be bigger) and the services we provide.
(there are two examples of what we like included in the pictures)
you can find more information o our website at pawplayhub@mailnest.example.

```html
<!DOCTYPE html>
<html lang="en">
<head>
<meta charset="utf-8">
<title>Bright Meadow Canine Activity Center – Billboard</title>
<link rel="stylesheet" href="https://fonts.googleapis.com/css2?family=Outfit:wght@500;600;700&display=swap">
<style>
  :root {
    --page-bg: #f4f4ec;
    --board-black: #161616;
    --lime: #84ff00;
    --white: #ffffff;
    --ink: #161616;
    --photo-light: #f3efe6;
    --photo-mid: #e2dbcc;
  }
  * { margin: 0; padding: 0; box-sizing: border-box; }
  html, body {
    width: 1200px; height: 900px; overflow: hidden;
    background: var(--page-bg);
    font-family: "Outfit", sans-serif;
  }
  .billboard {
    position: absolute; left: 0; top: 128px;
    width: 1200px; height: 644px;
    background: var(--board-black);
    overflow: hidden;
  }
  .accent-wedge { position: absolute; inset: 0; }
  .hero-photo {
    position: absolute; left: 858px; top: 22px;
    width: 336px; height: 622px;
    border-radius: 150px 150px 0 0;
    background: radial-gradient(ellipse at 50% 35%, var(--photo-light) 0%, var(--photo-mid) 100%);
  }
  .brand {
    position: absolute; left: 29px; top: 58px;
    color: var(--white); font-weight: 700; text-transform: uppercase;
    line-height: 1.1;
  }
  .brand-name { font-size: 34px; letter-spacing: 0.5px; }
  .brand-sub { font-size: 34px; display: block; font-size: 15px; letter-spacing: 1.6px; margin-top: 6px; }
  .headline {
    position: absolute; left: 28px; top: 206px;
    color: var(--white); font-weight: 700; font-size: 56px;
    line-height: 60px; letter-spacing: 0.3px;
  }
  .headline .highlight { color: var(--lime); }
  .services { list-style: none; }
  .service {
    position: absolute; width: 324px; height: 57px;
    background: var(--lime); border-radius: 20px;
    display: flex; align-items: center;
  }
  .service::before {
    content: ""; position: absolute; left: 76px; top: 0;
    width: 4px; height: 100%; background: var(--board-black);
  }
  .service-label {
    margin-left: 104px; color: var(--ink);
    font-weight: 600; font-size: 30px; letter-spacing: 0.6px;
  }
  .service--boarding { left: 29px; top: 339px; }
  .service--grooming { left: 407px; top: 339px; }
  .service--daycare { left: 29px; top: 434px; }
  .service--training { left: 407px; top: 434px; }
  .service--grooming .service-label,
  .service--training .service-label { margin-left: 110px; }
  .footer-name {
    position: absolute; left: 29px; top: 580px;
    color: var(--white); font-weight: 600; font-size: 29px; letter-spacing: 0.3px;
  }
  .contact {
    position: absolute; display: flex; align-items: center; gap: 10px;
    color: var(--white); font-weight: 600; font-size: 10.5px; line-height: 13px;
  }
  .contact--address { left: 327px; top: 583px; }
  .contact--web { left: 610px; top: 588px; }
  .contact svg { flex: none; }
</style>
</head>
<body>
  <section class="billboard">
    <svg class="accent-wedge" width="1200" height="644" viewBox="0 0 1200 644" aria-hidden="true">
      <polygon points="941,0 1200,0 1200,644 791,644" fill="var(--lime)"/>
    </svg>
    <div class="hero-photo" role="img" aria-label="Photo of a cream-coloured golden retriever puppy sitting and looking at the viewer"></div>

    <div class="brand">
      <span class="brand-name">Bright Meadow</span>
      <span class="brand-sub">Canine Activity Center</span>
    </div>

    <h1 class="headline">YOUR <span class="highlight">BEST FRIEND'S</span><br>BEST DAY</h1>

    <ul class="services">
      <li class="service service--boarding"><span class="service-label">BOARDING</span></li>
      <li class="service service--grooming"><span class="service-label">GROOMING</span></li>
      <li class="service service--daycare"><span class="service-label">DAYCARE</span></li>
      <li class="service service--training"><span class="service-label">TRAINING</span></li>
    </ul>

    <p class="footer-name">BRIGHT MEADOW</p>
    <div class="contact contact--address">
      <svg width="14" height="22" viewBox="0 0 14 22" aria-hidden="true">
        <path d="M7 0a7 7 0 0 0-7 7c0 5 7 15 7 15s7-10 7-15a7 7 0 0 0-7-7zm0 10a3 3 0 1 1 0-6 3 3 0 0 1 0 6z" fill="var(--white)"/>
      </svg>
      <span>48 ORCHARD LANE MAPLE<br>GROVE IA, 50200</span>
    </div>
    <div class="contact contact--web">
      <svg width="18" height="18" viewBox="0 0 18 18" aria-hidden="true" fill="none" stroke="var(--white)" stroke-width="1.3">
        <circle cx="9" cy="9" r="8"/>
        <ellipse cx="9" cy="9" rx="3.5" ry="8"/>
        <line x1="1" y1="9" x2="17" y2="9"/>
        <line x1="2.5" y1="5" x2="15.5" y2="5"/>
        <line x1="2.5" y1="13" x2="15.5" y2="13"/>
      </svg>
      <span>WWW.PAWPLAYHUB.EXAMPLE</span>
    </div>
  </section>
</body>
</html>
```